A website for Varnholt Limited

We need a new and modern website for our company. We are engineering consultants and contractors (EPC) in the oil and gas industry and building services industry.
What we do:
Engineering, procurement, construction
Automation (safety and process)
Non-destructive testing
Training
We have an existing website and the content can be referred from there since we are remaking the website
For more information visit Varnholt Limited Kenya

Coding

Number of Pages Required

1 page

```html
<!DOCTYPE html>
<html lang="en">
<head>
<meta charset="utf-8">
<title>Varnholt Limited</title>
<link href="https://fonts.googleapis.com/css2?family=Lato:wght@400;700&display=swap" rel="stylesheet">
<style>
  :root {
    --navy: #0a2763;
    --navy-deep: #061e55;
    --orange: #f7812f;
    --ink: #222222;
    --text: #444444;
    --white: #ffffff;
    --sky: #a7cdeb;
  }
  * { box-sizing: border-box; margin: 0; padding: 0; }
  html, body { width: 1023px; height: 1200px; overflow: hidden; background: var(--white); }
  body { font-family: "Lato", sans-serif; position: relative; }

  .hero { position: absolute; left: 0; top: 0; width: 1023px; height: 575px; background: linear-gradient(160deg, var(--navy) 0%, var(--navy-deep) 100%); overflow: hidden; }
  .hero-photo { position: absolute; inset: 0; }
  .hero-copy { position: absolute; left: 120px; top: 170px; width: 340px; color: var(--white); }
  .hero-title { font-size: 37px; font-weight: 700; line-height: 60px; letter-spacing: -0.3px; }
  .accent { color: var(--orange); }
  .hero-text { margin-top: 18px; font-size: 12px; line-height: 20px; }

  .btn { display: inline-block; background: var(--orange); color: var(--white); font-size: 14px; height: 36px; line-height: 36px; padding: 0 25px; border-radius: 18px; text-decoration: none; }
  .hero .btn { position: absolute; left: 115px; top: 392px; }

  .about { position: absolute; left: 0; top: 575px; width: 1023px; height: 475px; }
  .about-label { position: absolute; left: 126px; top: 122px; font-size: 12px; font-weight: 700; color: var(--orange); display: flex; align-items: center; gap: 8px; }
  .about-label::after { content: ""; width: 80px; height: 1px; background: var(--orange); }
  .about-title { position: absolute; left: 125px; top: 146px; font-size: 38px; font-weight: 700; color: var(--ink); letter-spacing: -0.3px; }
  .about-text { position: absolute; left: 126px; top: 203px; width: 340px; font-size: 12px; line-height: 20px; color: var(--text); }
  .about .btn { position: absolute; left: 122px; top: 299px; }

  .photo { position: absolute; border-radius: 8px; box-shadow: 0 10px 24px rgba(0,0,0,0.22); }
  .photo-team { left: 631px; top: 65px; width: 273px; height: 268px; background: linear-gradient(160deg, #c9ced3 0%, #7d8a7a 40%, #2a3140 70%, #3c5a2b 100%); }
  .photo-inspector { left: 559px; top: 219px; width: 147px; height: 195px; background: linear-gradient(170deg, #8b8776 0%, #3a3b36 50%, #3f7a2c 100%); }

  .stats { position: absolute; left: 0; top: 1050px; width: 1023px; height: 150px; background: var(--orange); color: var(--white); }
  .stat { position: absolute; top: 42px; width: 180px; margin-left: -90px; text-align: center; }
  .stat-num { font-size: 35px; font-weight: 700; line-height: 40px; }
  .stat-label { margin-top: 8px; font-size: 16px; }
</style>
</head>
<body>
  <section class="hero">
    <svg class="hero-photo" width="1023" height="575" viewBox="0 0 1023 575" role="img" aria-label="Engineer in a white hard hat pointing upward against the sky">
      <defs>
        <linearGradient id="heroSky" x1="0" y1="0" x2="0.4" y2="1">
          <stop offset="0" stop-color="#ffffff"/>
          <stop offset="0.35" stop-color="#e6eef5"/>
          <stop offset="0.55" stop-color="#8a8f99"/>
          <stop offset="0.75" stop-color="#1d1f26"/>
          <stop offset="1" stop-color="#15161b"/>
        </linearGradient>
        <linearGradient id="heroBlue" x1="0" y1="0" x2="1" y2="0">
          <stop offset="0" stop-color="#ffffff" stop-opacity="0"/>
          <stop offset="1" stop-color="var(--sky)" stop-opacity="0.8"/>
        </linearGradient>
      </defs>
      <polygon points="445,0 667,0 688,33 740,0 964,0 1008,70 931,122 1023,286 1023,575 757,575 700,500 640,575 564,575 520,490 600,430 490,285 535,190" fill="url(#heroSky)"/>
      <polygon points="740,0 964,0 1008,70 931,122 1023,286 1023,200 900,0" fill="url(#heroBlue)"/>
    </svg>
    <div class="hero-copy">
      <h1 class="hero-title">Start Your <span class="accent">Dream</span><br>Our <span class="accent">Professional</span></h1>
      <p class="hero-text">Lorem ipsum dolor sit amet, consectetuer adipiscing elit. Maecenas porttitor congue massa. Fusce posuere, magna sed pulvinar ultricies.</p>
    </div>
    <a class="btn" href="#">Contact Us</a>
  </section>

  <section class="about">
    <div class="about-label">About Us</div>
    <h2 class="about-title">We’re Professional</h2>
    <p class="about-text">Lorem ipsum dolor sit amet, consectetuer adipiscing elit. Maecenas porttitor congue massa. Fusce posuere, magna sed pulvinar ultricies.</p>
    <a class="btn" href="#">Contact Us</a>
    <div class="photo photo-team" role="img" aria-label="Team of engineers in safety helmets reviewing notes on site"></div>
    <div class="photo photo-inspector" role="img" aria-label="Engineer in a hard hat inspecting a ruined building"></div>
  </section>

  <section class="stats">
    <div class="stat" style="left:180px"><div class="stat-num">129</div><div class="stat-label">Project Done</div></div>
    <div class="stat" style="left:388px"><div class="stat-num">2130</div><div class="stat-label">Global Vendor</div></div>
    <div class="stat" style="left:597px"><div class="stat-num">32</div><div class="stat-label">Plan Project</div></div>
    <div class="stat" style="left:806px"><div class="stat-num">47</div><div class="stat-label">Certified</div></div>
  </section>
</body>
</html>
```